New Flyer Design Project

We need a flyer for our upcoming Rising Builders Forum.

5th Annual Rising Builders Forum
by the Council for Stewardship of Built Ventures (C-SBuV)
Theme: Step Forward
Date: January 24, 2020
Location: Bluestone Lodge Hotel and Conference Center, San Marcos, TX
#StepForward

This is event is put together by C-SBuV's Rising Builders Ring of Merit. I have a logo for the Ring of Merit, but not something that indicates it's the Rising Builders Ring.

More about the Forum (please don't include on the flyer): This Forum provides a venue to openly discuss issues affecting women in our industry and ideas and strategies to address those issues.

Architecture, Construction and Engineering are all struggling with a tremendous shortage of skilled talent. It is more important than ever for organizations to be able to attract, support and retain a talented workforce and to encourage more women to pursue and build vibrant careers in architecture, engineering and construction. Unfortunately, their attrition rate also remains high in these industries. Developing and retaining a skilled workforce includes identifying and addressing the specific needs of women in our industry. Man or Woman; Male or Female Brain, C-SBuV’s Rising Builders Forum will give you and your team the tools you need to excel as an Employer of Choice and a roadmap for individual continued career planning and success .

This unique Forum provides a venue to engage everyone from executives to those just beginning their careers with active, hands-on sessions and vibrant networking with the best and brightest in the A/E/C industry. In our usual C-SBuV Forum style, Keynotes become table participants and table participants become presenters, encouraging participants to assimilate what they are learning. Join local, state and national leaders and subject matter experts as we candidly explore and address the issues affecting women in our industry .

```html
<!DOCTYPE html>
<html lang="en">
<head>
<meta charset="utf-8">
<title>5th Annual Rising Builders Forum</title>
<link rel="stylesheet" href="https://fonts.googleapis.com/css2?family=Russo+One&family=Roboto+Slab:wght@800&family=Noto+Serif:wght@700&family=Signika:wght@400;500&display=swap">
<style>
  :root {
    --stage: #dfe6ee;
    --navy: #1f3f94;
    --navy-deep: #183379;
    --green: #8cbd3f;
    --band-gray: #4a4f5a;
    --white: #ffffff;
    --paper: #f6f6f6;
    --logo-gray: #555a62;
    --figure-coral: #efc3b4;
    --figure-orange: #f1c9ae;
    --figure-navy: #c9cfe3;
  }
  html, body {
    margin: 0;
    width: 1200px;
    height: 871px;
    overflow: hidden;
    background: var(--stage);
  }
  .flyer {
    position: absolute;
    left: 312px;
    top: 25px;
    width: 575px;
    height: 820px;
    background: var(--paper);
    overflow: hidden;
    box-shadow: 0 2px 10px rgba(0,0,0,0.12);
  }
  .flyer__header {
    position: absolute;
    inset: 0 0 auto 0;
    height: 480px;
    background: var(--navy);
  }
  .flyer__skyline {
    position: absolute;
    left: 0; right: 0;
    top: 255px;
    height: 225px;
    background: linear-gradient(180deg, rgba(24,51,121,0) 0%, var(--navy-deep) 45%, #16306f 100%);
  }
  .flyer__wave {
    position: absolute;
    left: 0; top: 380px;
    width: 575px; height: 120px;
  }
  .title {
    position: absolute;
    left: 0; right: 0;
    text-align: center;
    margin: 0;
    font-family: "Russo One", sans-serif;
    font-weight: 400;
    line-height: 1;
  }
  .title__line1 { top: 38px; font-size: 38px; color: var(--white); }
  .title__line2 { top: 82px; font-size: 40px; color: var(--green); }
  .host-pill {
    position: absolute;
    left: 43px; top: 138px;
    width: 487px; height: 34px;
    border-radius: 10px;
    background: var(--green);
    color: var(--white);
    font-family: "Signika", sans-serif;
    font-weight: 500;
    font-size: 16px;
    line-height: 34px;
    text-align: center;
  }
  .theme {
    position: absolute;
    left: 0; right: 0; top: 192px;
    margin: 0;
    text-align: center;
    font-family: "Roboto Slab", serif;
    font-weight: 800;
    font-size: 56px;
    line-height: 1;
    color: var(--white);
    letter-spacing: -1px;
  }
  .date {
    position: absolute;
    left: 0; right: 0; top: 256px;
    text-align: center;
    font-family: "Noto Serif", serif;
    font-weight: 700;
    font-size: 30px;
    line-height: 1.2;
    color: var(--green);
  }
  .venue__pin {
    position: absolute;
    left: 280px; top: 310px;
    width: 14px; height: 18px;
  }
  .venue {
    position: absolute;
    left: 0; right: 0; top: 332px;
    margin: 0;
    text-align: center;
    font-family: "Signika", sans-serif;
    font-size: 19px;
    line-height: 21px;
    color: var(--white);
  }
  .brand {
    position: absolute;
    top: 452px; left: 0; right: 0;
    display: flex;
    justify-content: center;
    align-items: center;
    gap: 18px;
  }
  .brand__circle {
    width: 66px; height: 66px;
    border-radius: 50%;
    background: var(--navy);
  }
  .brand__name {
    font-family: "Signika", sans-serif;
    font-weight: 400;
    font-size: 40px;
    color: var(--logo-gray);
  }
  .flyer__people {
    position: absolute;
    left: 28px; right: 25px;
    top: 538px; bottom: 14px;
    background:
      linear-gradient(180deg, var(--paper) 0%, rgba(246,246,246,0) 30%, rgba(246,246,246,0) 85%, var(--paper) 100%),
      linear-gradient(90deg, var(--paper) 0%, var(--figure-coral) 10%, var(--figure-orange) 30%, var(--figure-navy) 50%, var(--figure-orange) 70%, var(--figure-coral) 90%, var(--paper) 100%);
  }
</style>
</head>
<body>
  <main class="flyer">
    <section class="flyer__header">
      <div class="flyer__skyline" role="img" aria-label="Navy city skyline of tall office towers"></div>

      <h1 class="title title__line1">5TH ANNUAL RISING</h1>
      <h1 class="title title__line2">BUILDERS FORUM</h1>

      <div class="host-pill">by the Council for Stewardship of Built Ventures (C-SBuV)</div>

      <p class="theme">STEP FORWARD</p>
      <div class="date">January 24, 2020</div>

      <svg class="venue__pin" viewBox="0 0 14 18" aria-hidden="true">
        <path d="M7 1a5.5 5.5 0 0 0-5.5 5.5C1.5 11 7 17 7 17s5.5-6 5.5-10.5A5.5 5.5 0 0 0 7 1z" fill="none" stroke="#8cbd3f" stroke-width="2"/>
        <circle cx="7" cy="6.5" r="1.8" fill="#8cbd3f"/>
      </svg>
      <p class="venue">Bluestone Lodge Hotel and Conference Center,<br>San Marcos, TX</p>
    </section>

    <svg class="flyer__wave" viewBox="0 0 575 120" preserveAspectRatio="none" aria-hidden="true">
      <path d="M0 55 Q287 -25 575 55 L575 120 L0 120 Z" fill="#4a4f5a"/>
      <path d="M0 70 Q287 0 575 70 L575 120 L0 120 Z" fill="#8cbd3f"/>
      <path d="M0 80 Q287 20 575 80 L575 120 L0 120 Z" fill="#f6f6f6"/>
    </svg>

    <div class="brand">
      <span class="brand__circle"></span>
      <span class="brand__name">C-SBuV</span>
    </div>

    <div class="flyer__people" role="img" aria-label="Illustration of five professional women standing in a row holding folders and tablets"></div>
  </main>
</body>
</html>
```